Korvane Nutrition Label Design

I need a label design for private label nutritional supplements.

I only need the middle section of a three part label. The ingredient information will be inserted into the left and ride side of the vector file by the manufacturer. The entire label is 15.5 cm wide by 6.3 cm tall. The space in the middle where the this label design will go is 6.3 x 6.3 cm.

I have an example of a label I have created but want replaced with a better version (-original_IMG_0949.jpeg).

I would like the label modeled on sn1792.jpg. Or modeled on berberine.jpg. I need three logos on the label: nowledge-gmp-logo-thumb-2x.jpg, non-gmo.gif, and the company logo you see at the top of the -original_IMG_0949.jpeg file (I uploaded Logo-Korvane Nutrition.jpg as an example of the company logo that was changed in the -original_IMG_0949.jpeg file). The logo should say Korvane Nutrition (trademark symbol), not Korvane Nutrition for this label.

In addition to the three logos, the label must have the company tagline "Which Tonics Suit Your Routine?" (trademark symbol). It must also say "DIETARY SUPPLEMENT"

- Use the colors from the Korvane Nutrition logo to create the label

For graphics, you can try to use the two pixelmarsh files I uploaded of the molecules. Be creative if you have an idea.

The label also must contain the following claims as you see in the -original_IMG_0949.jpg file:
Supports Dental Health* | Structural Support*
Helps Maintain Strong Bones*

The label must also feature the name of the supplement:
High Potency
Vitamin D-3
1000 IU
180 Softgels

Target Market(s)

New Supplements Users age 20-45

Industry/Entity Type

Nutrition

Requirements
Must have
• The project must have three logos on the label:
• 1) the company logo
• 2) the non-gmo logo
• 3) the GMP logo
• The label must have text for the name of the supplement:
• High Potency
• Vitamin D-3
• 1000 IU
• 180 Softgels
• The label must have the following claims:
• Supports Dental Health* | Structural Support*
• Helps Maintain Strong Bones*
• Final deliverable needs to be Photoshop Illustrator

```html
<!DOCTYPE html>
<html lang="en">
<head>
<meta charset="utf-8">
<title>Korvane Nutrition Vitamin D3 Label</title>
<link rel="stylesheet" href="https://fonts.googleapis.com/css2?family=Roboto+Condensed:ital,wght@0,400;0,700;1,400;1,700&display=swap">
<style>
  :root{
    --stage:#76a0b0;
    --paper:#ffffff;
    --brand-blue:#1372bd;
    --brand-green:#1f9d55;
    --hex-ring:#3fae6a;
    --badge-purple:#4a4f9c;
    --art-light:#e6eef5;
    --art-mid:#b9cfe0;
  }
  *{margin:0;padding:0;box-sizing:border-box}
  html,body{width:1200px;height:1200px;overflow:hidden}
  body{background:var(--stage);position:relative;font-family:"Roboto Condensed",sans-serif}
  .label{position:absolute;left:30px;top:368px;width:1140px;height:463px;background:var(--paper);border-top:6px solid var(--brand-blue);overflow:hidden}
  .brand{position:absolute;left:356px;top:28px;display:flex;align-items:center;gap:8px;z-index:2}
  .brand-dot{width:28px;height:28px;border-radius:50%;background:var(--brand-green)}
  .brand-name{font-weight:700;font-size:23px;color:var(--brand-blue);line-height:1}
  .brand-name sup{font-size:10px;vertical-align:top}
  .brand-tagline{font-size:8px;letter-spacing:.3px;color:#8a8f96;text-transform:uppercase;margin-top:2px}
  .category-pill{position:absolute;left:356px;top:95px;width:192px;height:28px;border-radius:14px;background:var(--brand-green);color:#fff;font-weight:700;font-size:14px;letter-spacing:2.4px;display:flex;align-items:center;justify-content:center;z-index:2}
  .hero-art{position:absolute;left:640px;top:4px;width:170px;height:401px;z-index:1;background:radial-gradient(ellipse at 55% 50%,var(--art-mid),var(--art-light) 55%,rgba(255,255,255,0) 78%)}
  .product-badge{position:absolute;left:370px;top:153px;width:286px;height:148px;z-index:3}
  .product-name{position:absolute;left:370px;top:153px;width:286px;height:148px;display:flex;flex-direction:column;align-items:center;justify-content:center;color:#fff;font-style:italic;line-height:1;z-index:4}
  .product-name .potency{font-size:20px;margin-left:-40px}
  .product-name .vitamin{font-weight:700;font-size:34px;letter-spacing:-.5px}
  .product-name .vitamin b{font-size:56px;letter-spacing:-1px;margin-left:2px}
  .product-name .dose{font-size:28px;margin-top:-6px}
  .product-name .dose sup{font-size:13px}
  .cert-row{position:absolute;left:359px;top:335px;display:flex;align-items:center;gap:15px;z-index:2}
  .cert{width:43px;height:43px;border-radius:50%}
  .cert.gmp{background:var(--badge-purple)}
  .cert.non-gmo{background:var(--brand-green)}
  .count{font-size:19px;color:var(--brand-green)}
  .claims-band{position:absolute;left:0;bottom:0;width:100%;height:54px;background:var(--brand-blue);color:#fff;font-weight:700;font-size:13px;text-align:center;display:flex;flex-direction:column;justify-content:center;line-height:1.25;z-index:5}
</style>
</head>
<body>
  <section class="label">
    <div class="brand">
      <span class="brand-dot"></span>
      <div>
        <div class="brand-name">Korvane Nutrition<sup>™</sup></div>
        <div class="brand-tagline">Which Tonics Suit Your Routine?™</div>
      </div>
    </div>

    <div class="category-pill">DIETARY SUPPLEMENT</div>

    <div class="hero-art" role="img" aria-label="Illustration of a human figure made of molecules beside a DNA helix"></div>

    <svg class="product-badge" viewBox="0 0 286 148" aria-hidden="true">
      <polygon points="34,2 252,2 284,74 252,146 34,146 2,74" fill="none" stroke="var(--hex-ring)" stroke-width="3"/>
      <polygon points="38,8 248,8 277,74 248,140 38,140 9,74" fill="var(--brand-blue)"/>
    </svg>
    <div class="product-name">
      <span class="potency">High Potency</span>
      <span class="vitamin">VITAMIN<b>D3</b></span>
      <span class="dose">1000<sup>IU</sup></span>
    </div>

    <div class="cert-row">
      <span class="cert gmp" role="img" aria-label="GMP quality badge"></span>
      <span class="cert non-gmo" role="img" aria-label="Non-GMO badge"></span>
      <span class="count">180 softgels</span>
    </div>

    <div class="claims-band">
      <span>Supports Dental Health* | Structural Support*</span>
      <span>Helps Maintain Strong Bones*</span>
    </div>
  </section>
</body>
</html>
```